Quality Improvement Software for healthcare agencies needs a website.

Veltrix820 is a software for hospices and home health agencies to manage their Quality Assurance Performance Improvement programs to remain complaint with the standards set by Sanovia and the Bureau of Civic Wellbeing. The web accessible software-as-a-service provides an easy, turn-key way for agencies to organize all the information they need to manage and track.

Coded - Design and coding required

4 page

```html
<!DOCTYPE html>
<html lang="en">
<head>
<meta charset="utf-8">
<title>Veltrix820 — Quality Assurance Performance Improvement</title>
<link href="https://fonts.googleapis.com/css2?family=Open+Sans:wght@400;600;700;800&family=Montserrat:wght@500;600&display=swap" rel="stylesheet">
<style>
:root{
  --navy:#1b365d;
  --navy-dark:#172c4b;
  --orange:#f7931e;
  --green:#6ab023;
  --blue:#29a9e1;
  --grey:#ebebeb;
  --ink:#111;
  --white:#fff;
}
*{box-sizing:border-box;margin:0;padding:0}
html,body{width:1200px;height:3826px;overflow:hidden}
body{font-family:"Open Sans",sans-serif;color:var(--ink);background:var(--white);position:relative}
section,header,footer,.topbar{position:absolute;left:0;width:1200px}
.abs{position:absolute}

/* top bar */
.topbar{top:0;height:43px;background:var(--navy-dark);color:var(--white);font-size:13px;font-weight:600}
.topbar .item{position:absolute;top:9px;display:flex;align-items:center;gap:8px}
.dot-icon{width:24px;height:24px;border-radius:50%;background:#f5c400;display:flex;align-items:center;justify-content:center}
.social{position:absolute;right:144px;top:9px;display:flex;gap:5px}
.social span{width:26px;height:26px;border-radius:50%;background:var(--blue);border:2px solid var(--white)}

/* header */
.site-header{top:43px;height:83px;background:var(--white)}
.brand{position:absolute;left:144px;top:20px;display:flex;align-items:center;gap:10px;font-family:"Montserrat",sans-serif;font-weight:600;font-size:34px;color:var(--navy)}
.brand .mark{width:30px;height:30px;background:var(--orange)}
.nav{position:absolute;left:455px;top:34px;display:flex;gap:22px;font-size:14px;font-weight:600;color:var(--navy)}
.call{position:absolute;left:873px;top:20px;display:flex;align-items:center;gap:8px}
.call .ring{width:36px;height:36px;border-radius:50%;background:var(--orange);display:flex;align-items:center;justify-content:center}
.call small{display:block;font-size:13px;color:var(--navy);font-weight:600}
.call b{display:block;font-size:20px;color:var(--navy);font-weight:700;line-height:1.1}

/* hero */
.hero{top:126px;height:640px;background:linear-gradient(90deg,#4b5f7c,#7d8ea6 50%,#55698a)}
.hero::after{content:"";position:absolute;inset:0;background:rgba(27,54,93,.45)}
.hero-title{position:absolute;z-index:2;width:100%;text-align:center;top:64px;font-family:"Montserrat",sans-serif;font-weight:600;font-size:108px;color:var(--white);line-height:1}
.hero-sub{position:absolute;z-index:2;width:100%;text-align:center;top:198px;font-size:31px;font-weight:700;color:var(--white)}
.band{top:766px;height:223px;background:var(--grey)}

/* laptop mockup (hero) */
.laptop{position:absolute;z-index:3;left:264px;top:401px;width:672px;height:416px}
.laptop .screen{position:absolute;left:44px;top:0;width:584px;height:376px;border-radius:8px 8px 0 0;border:4px solid #2b2b2b;background:#f4f6f9;overflow:hidden}
.laptop .screen-band{position:absolute;left:0;top:259px;width:100%;height:120px;background:var(--navy)}
.laptop .base{position:absolute;left:0;top:372px;width:672px;height:26px;background:#333;border-radius:0 0 16px 16px}
.mini-portrait{position:absolute;left:65px;top:29px;width:196px;height:196px;border-radius:50%;border:3px solid var(--navy);padding:6px;background:var(--white)}
.mini-portrait div{width:100%;height:100%;border-radius:50%;background:linear-gradient(160deg,#dbe4ee,#6f87a6)}
.mini-mark{position:absolute;width:22px;height:22px;border-radius:3px;background:var(--orange)}
.mini-title{position:absolute;left:278px;top:70px;font-size:18px;font-weight:800;color:var(--navy);line-height:1.2}
.mini-text{position:absolute;left:278px;width:232px;font-size:6.5px;line-height:1.5;text-align:justify}
.mini-btn{position:absolute;left:278px;top:198px;width:62px;height:20px;border-radius:10px;background:var(--navy);color:var(--white);font-size:8px;font-weight:700;display:flex;align-items:center;justify-content:center}
.mini-testi{position:absolute;left:0;width:100%;text-align:center;top:318px;font-size:16px;font-weight:800;color:var(--white)}

.features{position:absolute;top:854px;left:144px;display:flex}
.feature{width:316px;display:flex;gap:13px}
.feature .ic{width:86px;height:86px;border-radius:50%;display:flex;align-items:center;justify-content:center;flex:none;border:3px solid rgba(255,255,255,.6)}
.feature h3{font-size:27px;font-weight:600;color:var(--navy);line-height:1.1}
.feature p{font-size:13px;line-height:1.4;margin-top:5px}

/* section heading */
.sec-mark{position:absolute;left:50%;width:50px;height:50px;margin-left:-25px;border-radius:6px}
.sec-title{position:absolute;width:100%;text-align:center;font-weight:800;font-size:37px;color:var(--navy)}

/* services */
.services{top:989px;height:704px}
.services .lead{position:absolute;left:180px;width:840px;top:144px;text-align:center;font-size:13px;line-height:1.6}
.card{position:absolute;top:220px;width:286px;height:423px;border:1.5px solid #333;border-radius:10px;text-align:center}
.card .photo{position:absolute;left:9px;top:9px;width:266px;height:200px;border-radius:6px;background:linear-gradient(135deg,#c9d6e4,#8fa4bd)}
.card .badge{position:absolute;left:100px;top:166px;width:86px;height:86px;border-radius:50%;border:5px solid var(--white);display:flex;align-items:center;justify-content:center}
.card h3{position:absolute;top:262px;left:0;width:100%;font-size:21px;font-weight:600;line-height:1.15;color:var(--ink)}
.card p{position:absolute;top:320px;left:16px;width:252px;font-size:13px;line-height:1.6}

/* about */
.about{top:1693px;height:638px;background:linear-gradient(90deg,var(--navy) 45%,#3f5879);overflow:hidden}
.about h2{position:absolute;left:144px;top:173px;font-size:37px;font-weight:800;color:var(--white)}
.about .copy-block{position:absolute;left:144px;width:380px;font-size:13px;line-height:1.6;color:var(--white);font-weight:600;text-align:justify}
.btn{position:absolute;display:flex;align-items:center;justify-content:center;border-radius:24px;font-weight:700;font-size:17px}

/* about: laptop with site preview */
.shot{position:absolute;left:554px;top:74px;width:700px;height:500px}
.shot .screen{position:absolute;left:52px;top:0;width:620px;height:436px;border:4px solid #2b2b2b;border-radius:8px 0 0 0;overflow:hidden;background:linear-gradient(90deg,#3e5474,#6c7f9b 55%,#4a5f80)}
.shot .base{position:absolute;left:0;top:432px;width:700px;height:24px;background:#333;border-radius:0 0 0 14px}
.pv-head{position:absolute;left:0;top:0;width:100%;height:42px;background:var(--white)}
.pv-brand{position:absolute;left:70px;top:11px;display:flex;align-items:center;gap:5px;font-family:"Montserrat",sans-serif;font-weight:600;font-size:17px;color:var(--navy)}
.pv-brand span{width:11px;height:11px;background:var(--orange)}
.pv-nav{position:absolute;left:230px;top:17px;display:flex;gap:10px;font-size:7px;font-weight:700;color:var(--navy)}
.pv-call{position:absolute;left:456px;top:10px;display:flex;align-items:center;gap:4px;font-size:8px;font-weight:700;color:var(--navy);line-height:1.1}
.pv-call i{width:16px;height:16px;border-radius:50%;background:var(--orange)}
.pv-title{position:absolute;left:0;width:624px;top:78px;text-align:center;font-family:"Montserrat",sans-serif;font-weight:600;font-size:58px;line-height:1;color:var(--white)}
.pv-sub{position:absolute;left:0;width:624px;top:150px;text-align:center;font-size:16px;font-weight:700;color:var(--white)}
.pv-laptop{position:absolute;left:156px;top:188px;width:312px;height:222px;border:3px solid #2b2b2b;border-radius:5px 5px 0 0;background:#f4f6f9;overflow:hidden}
.pv-laptop .band2{position:absolute;left:0;top:138px;width:100%;height:90px;background:var(--navy)}
.pv-circle{position:absolute;left:36px;top:20px;width:100px;height:100px;border-radius:50%;border:2px solid var(--navy);padding:4px;background:var(--white)}
.pv-circle div{width:100%;height:100%;border-radius:50%;background:linear-gradient(160deg,#dbe4ee,#6f87a6)}
.pv-h{position:absolute;left:150px;top:30px;font-size:9px;font-weight:800;color:var(--navy);line-height:1.2}
.pv-t{position:absolute;left:150px;top:56px;width:135px;font-size:4.5px;line-height:1.5}
.pv-b{position:absolute;left:150px;top:90px;width:30px;height:9px;border-radius:5px;background:var(--navy)}
.pv-ts{position:absolute;left:0;width:100%;top:178px;text-align:center;font-size:9px;font-weight:800;color:var(--white)}
.pv-strip{position:absolute;left:0;top:410px;width:100%;height:30px;background:var(--grey)}
.pv-base2{position:absolute;left:140px;top:406px;width:344px;height:10px;background:#333;border-radius:0 0 8px 8px}

/* improving */
.improve{top:2331px;height:535px}
.improve .portrait{position:absolute;left:144px;top:64px;width:406px;height:406px;border-radius:50%;border:4px solid var(--navy);padding:12px;background:var(--white)}
.improve .portrait div{width:100%;height:100%;border-radius:50%;background:linear-gradient(160deg,#dbe4ee,#6f87a6)}
.improve h2{position:absolute;left:581px;top:160px;font-size:38px;font-weight:800;color:var(--navy);line-height:1.18}
.improve p{position:absolute;left:581px;width:474px;font-size:13px;line-height:1.6;text-align:justify}

/* testimonials */
.testimonials{top:2866px;height:603px;background:linear-gradient(90deg,var(--navy),#2e4a72 55%,var(--navy))}
.tcard{position:absolute;top:264px;width:440px;height:207px;background:var(--white);border-radius:10px;text-align:center}
.tcard .avatar{position:absolute;left:178px;top:-44px;width:84px;height:84px;border-radius:50%;border:4px solid var(--white);background:linear-gradient(160deg,#c8d3df,#5d6f86)}
.tcard p{position:absolute;top:60px;left:22px;width:396px;font-size:16px;font-weight:600;line-height:1.4}
.stars{position:absolute;top:168px;left:0;width:100%;display:flex;justify-content:center}
.dots{position:absolute;top:526px;left:0;width:100%;display:flex;justify-content:center;gap:12px}
.dots span{width:12px;height:12px;border-radius:50%;background:var(--white)}

/* footer */
.site-footer{top:3469px;height:357px}
.f-brand{position:absolute;left:144px;top:94px;font-family:"Montserrat",sans-serif;font-weight:600;font-size:42px;color:var(--navy)}
.f-brand-mark{position:absolute;left:222px;top:40px;width:44px;height:44px;background:var(--orange)}
.f-col{position:absolute;top:76px}
.f-col h4{font-size:21px;font-weight:600;color:var(--navy);margin-bottom:12px}
.f-col li{list-style:none;font-size:15px;font-weight:600;line-height:1.7;color:var(--navy)}
.contact-row{display:flex;gap:10px;align-items:flex-start;font-size:15px;font-weight:600;color:var(--navy);margin-bottom:14px;line-height:1.3}
.contact-row .ci{width:30px;height:30px;border-radius:50%;background:var(--navy);flex:none;display:flex;align-items:center;justify-content:center}
.field{width:228px;height:39px;border:1.5px solid #333;border-radius:3px;font-size:14px;padding:10px;margin-bottom:10px;color:var(--ink)}
.rule{position:absolute;left:144px;top:284px;width:912px;height:1px;background:#999}
.copy{position:absolute;top:311px;width:100%;text-align:center;font-size:13px}
</style>
</head>
<body>

<svg width="0" height="0" style="position:absolute"><defs><path id="star" d="M10 1l2.6 5.6 6 .7-4.5 4.1 1.2 6L10 14.4 4.7 17.4l1.2-6L1.4 7.3l6-.7z"/></defs></svg>

<div class="topbar">
  <div class="item" style="left:144px"><span class="dot-icon"><svg width="12" height="10" viewBox="0 0 12 10"><rect x="0.5" y="0.5" width="11" height="9" fill="none" stroke="#172c4b"/><path d="M1 1l5 4 5-4" fill="none" stroke="#172c4b"/></svg></span>hello@veltrix820.io</div>
  <div class="item" style="left:344px"><span class="dot-icon"><svg width="10" height="13" viewBox="0 0 10 13"><path d="M5 12S1 7 1 4.5a4 4 0 018 0C9 7 5 12 5 12z" fill="none" stroke="#172c4b" stroke-width="1.4"/><circle cx="5" cy="4.5" r="1.4" fill="#172c4b"/></svg></span>14 Harbor Lane, Eastfield</div>
  <div class="social"><span></span><span></span><span></span></div>
</div>

<header class="site-header">
  <div class="brand"><span class="mark"></span>Veltrix820</div>
  <nav class="nav"><span>HOME</span><span>ABOUT</span><span>PAGES</span><span>SHOP</span><span>BLOG</span><span>CONTACT</span></nav>
  <div class="call"><span class="ring"><svg width="18" height="18" viewBox="0 0 24 24"><path d="M6.6 10.8a15 15 0 006.6 6.6l2.2-2.2a1 1 0 011-.25 11.4 11.4 0 003.6.6 1 1 0 011 1V20a1 1 0 01-1 1A17 17 0 013 4a1 1 0 011-1h3.5a1 1 0 011 1c0 1.25.2 2.45.6 3.6a1 1 0 01-.25 1z" fill="#1b365d"/></svg></span><div><small>Call Anytime</small><b>555 0147 2290</b></div></div>
</header>

<section class="hero" role="img" aria-label="Background photo of smiling healthcare staff">
  <h1 class="hero-title">Veltrix820</h1>
  <p class="hero-sub">Quality Assurance Performance Improvement programs</p>
</section>
<section class="band"></section>

<div class="laptop">
  <div class="screen">
    <div class="mini-portrait" role="img" aria-label="Photo of a smiling doctor"><div></div></div>
    <span class="mini-mark" style="left:278px;top:42px"></span>
    <div class="mini-title">Improving Health in Your<br>Communities</div>
    <p class="mini-text" style="top:122px">Lorem ipsum dolor sit amet conse ctetur adipiscing elit, sed do eiusmod tempor incididunt ut labore et dolore magna aliqua quis ipsum suspendisse ultrices gravida.</p>
    <p class="mini-text" style="top:158px">Lorem ipsum dolor sit amet conse ctetur adipiscing elit, sed do eiusmod tempor incididunt ut labore et dolore magna aliqua quis ipsum suspendisse ultrices gravida.</p>
    <span class="mini-btn">Read More</span>
    <div class="screen-band"></div>
    <span class="mini-mark" style="left:281px;top:288px;width:22px;height:22px;background:var(--white)"></span>
    <div class="mini-testi">Our Testimonials</div>
  </div>
  <div class="base"></div>
</div>

<div class="features">
  <div class="feature"><span class="ic" style="background:var(--blue)"><svg width="44" height="44" viewBox="0 0 44 44"><circle cx="22" cy="22" r="17" fill="none" stroke="#fff" stroke-width="3"/><path d="M14 22l6 6 11-12" fill="none" stroke="#fff" stroke-width="3.5"/></svg></span><div><h3>Quality</h3><p>Home health agencies to<br>manage their Quality<br>Assurance Performance</p></div></div>
  <div class="feature"><span class="ic" style="background:var(--green)"><svg width="44" height="44" viewBox="0 0 44 44"><path d="M22 5l14 5v11c0 9-6 15-14 18C14 36 8 30 8 21V10z" fill="none" stroke="#fff" stroke-width="3"/><path d="M15 22l5 5 9-10" fill="none" stroke="#fff" stroke-width="3"/></svg></span><div><h3>Assurance</h3><p>Home health agencies to<br>manage their Quality<br>Assurance Performance</p></div></div>
  <div class="feature"><span class="ic" style="background:var(--orange)"><svg width="44" height="44" viewBox="0 0 44 44"><rect x="8" y="28" width="5" height="10" fill="#fff"/><rect x="17" y="22" width="5" height="16" fill="#fff"/><rect x="26" y="16" width="5" height="22" fill="#fff"/><path d="M7 22l10-8 7 5 12-12" fill="none" stroke="#fff" stroke-width="3"/></svg></span><div><h3>Performance</h3><p>Home health agencies to<br>manage their Quality<br>Assurance Performance</p></div></div>
</div>

<section class="services">
  <span class="sec-mark" style="top:34px;background:var(--green)"></span>
  <h2 class="sec-title" style="top:90px">Our Services</h2>
  <p class="lead">Lorem ipsum dolor sit amet conse ctetur adipiscing elit, sed do eiusmod tempor incididunt ut labore et dolore magna aliqua quis ipsum suspendisse ultrices gravida.</p>

  <article class="card" style="left:144px">
    <div class="photo" role="img" aria-label="Photo of a team of nurses"></div>
    <span class="badge" style="background:var(--blue)"><svg width="40" height="40" viewBox="0 0 40 40"><rect x="9" y="7" width="22" height="28" rx="2" fill="none" stroke="#1b365d" stroke-width="2.5"/><rect x="15" y="4" width="10" height="6" fill="#1b365d"/><path d="M14 18h12M14 24h12M14 30h8" stroke="#1b365d" stroke-width="2"/></svg></span>
    <h3>Bureau of Civic<br>Wellbeing</h3>
    <p>Lorem ipsum dolor sit amet conse ctetur adipiscing elit, sed do eiusmod tempor incididunt ut labore et dolore magna aliqua quis ipsum.</p>
  </article>
  <article class="card" style="left:457px">
    <div class="photo" role="img" aria-label="Photo of doctors reviewing notes"></div>
    <span class="badge" style="background:var(--green)"><svg width="40" height="40" viewBox="0 0 40 40"><path d="M20 22s-8-5-8-10a4 4 0 018-1 4 4 0 018 1c0 5-8 10-8 10z" fill="none" stroke="#1b365d" stroke-width="2.5"/><path d="M5 24c4 0 8 6 15 8 7-2 11-8 15-8" fill="none" stroke="#1b365d" stroke-width="2.5"/></svg></span>
    <h3>Bureau of Civic<br>Wellbeing</h3>
    <p>Lorem ipsum dolor sit amet conse ctetur adipiscing elit, sed do eiusmod tempor incididunt ut labore et dolore magna aliqua quis ipsum.</p>
  </article>
  <article class="card" style="left:769px">
    <div class="photo" role="img" aria-label="Photo of a nurse with a tablet"></div>
    <span class="badge" style="background:var(--orange)"><svg width="40" height="40" viewBox="0 0 40 40"><rect x="8" y="6" width="20" height="26" rx="2" fill="none" stroke="#1b365d" stroke-width="2.5"/><path d="M12 13h12M12 19h8" stroke="#1b365d" stroke-width="2"/><path d="M28 22l7 3v5c0 4-3 6-7 8-4-2-7-4-7-8v-5z" fill="#fff" stroke="#1b365d" stroke-width="2"/></svg></span>
    <h3>Bureau of Civic<br>Wellbeing</h3>
    <p>Lorem ipsum dolor sit amet conse ctetur adipiscing elit, sed do eiusmod tempor incididunt ut labore et dolore magna aliqua quis ipsum.</p>
  </article>
</section>

<section class="about">
  <span class="abs" style="left:144px;top:104px;width:56px;height:52px;border-radius:6px;background:var(--white)"></span>
  <h2>About QAP</h2>
  <p class="copy-block" style="top:245px">Veltrix820 is a software for hospices and home health agencies to manage their Quality Assurance Performance Improvement programs to remain complaint with the standards set by Sanovia and the Bureau of Civic Wellbeing. The web accessible software-as-a-service provides an easy, turn-key way for agencies to organize all the information they need to manage and track.</p>
  <p class="copy-block" style="top:413px">Lorem ipsum dolor sit amet conse ctetur adipiscing elit, sed do eiusmod tempor incididunt ut labore et dolore magna aliqua quis ipsum suspendisse ultrices gravida.</p>
  <span class="btn" style="left:144px;top:494px;width:128px;height:47px;background:var(--white);color:var(--navy)">Read More</span>

  <div class="shot">
    <div class="screen">
      <div class="pv-head">
        <div class="pv-brand"><span></span>Veltrix820</div>
        <div class="pv-nav"><span>HOME</span><span>ABOUT</span><span>PAGES</span><span>SHOP</span><span>BLOG</span><span>CONTACT</span></div>
        <div class="pv-call"><i></i><div>Call Anytime<br>555 0147 2290</div></div>
      </div>
      <div class="pv-title">Veltrix820</div>
      <div class="pv-sub">Quality Assurance Performance Improvement programs</div>
      <div class="pv-strip"></div>
      <div class="pv-laptop">
        <div class="pv-circle" role="img" aria-label="Photo of a smiling doctor"><div></div></div>
        <div class="pv-h">Improving Health in Your<br>Communities</div>
        <p class="pv-t">Lorem ipsum dolor sit amet conse ctetur adipiscing elit, sed do eiusmod tempor incididunt.</p>
        <span class="pv-b"></span>
        <div class="band2"></div>
        <div class="pv-ts">Our Testimonials</div>
      </div>
      <div class="pv-base2"></div>
    </div>
    <div class="base"></div>
  </div>
</section>

<section class="improve">
  <div class="portrait" role="img" aria-label="Photo of a smiling doctor with a stethoscope"><div></div></div>
  <span class="abs" style="left:581px;top:90px;width:56px;height:56px;border-radius:6px;background:var(--orange)"></span>
  <h2>Improving Health in Your<br>Communities</h2>
  <p style="top:260px">Lorem ipsum dolor sit amet conse ctetur adipiscing elit, sed do eiusmod tempor incididunt ut labore et dolore magna aliqua quis ipsum suspendisse ultrices gravida.</p>
  <p style="top:332px">Lorem ipsum dolor sit amet conse ctetur adipiscing elit, sed do eiusmod tempor incididunt ut labore et dolore magna aliqua quis ipsum suspendisse ultrices gravida.</p>
  <span class="btn" style="left:581px;top:404px;width:128px;height:44px;background:var(--navy);color:var(--white)">Read More</span>
</section>

<section class="testimonials">
  <span class="sec-mark" style="top:52px;width:58px;height:58px;margin-left:-29px;background:var(--white)"></span>
  <h2 class="sec-title" style="top:122px;color:var(--white)">Our Testimonials</h2>
  <div class="tcard" style="left:143px">
    <div class="avatar" role="img" aria-label="Client portrait"></div>
    <p>Lorem ipsum dolor sit amet conse ctetur adipiscing elit, sed do eiusmod tempor incididunt ut labore et dolore magna aliqua quis ipsum suspendisse ultrices gravida.</p>
    <div class="stars"><svg width="140" height="20" viewBox="0 0 140 20"><g fill="#f7931e"><use href="#star"/><use href="#star" x="28"/><use href="#star" x="56"/><use href="#star" x="84"/></g><use href="#star" x="112" fill="#fbd7a8"/></svg></div>
  </div>
  <div class="tcard" style="left:616px">
    <div class="avatar" role="img" aria-label="Client portrait"></div>
    <p>Lorem ipsum dolor sit amet conse ctetur adipiscing elit, sed do eiusmod tempor incididunt ut labore et dolore magna aliqua quis ipsum suspendisse ultrices gravida.</p>
    <div class="stars"><svg width="140" height="20" viewBox="0 0 140 20"><g fill="#f7931e"><use href="#star"/><use href="#star" x="28"/><use href="#star" x="56"/><use href="#star" x="84"/></g><use href="#star" x="112" fill="#fbd7a8"/></svg></div>
  </div>
  <div class="dots"><span></span><span></span><span></span></div>
</section>

<footer class="site-footer">
  <span class="f-brand-mark"></span>
  <div class="f-brand">Veltrix820</div>
  <div class="f-col" style="left:397px"><h4>Quick Links</h4><ul><li>Home</li><li>About Us</li><li>Services</li><li>Blog</li><li>Contact Us</li></ul></div>
  <div class="f-col" style="left:564px"><h4>Contact Us</h4>
    <div class="contact-row"><span class="ci"><svg width="14" height="11" viewBox="0 0 12 10"><rect x="0.5" y="0.5" width="11" height="9" fill="none" stroke="#fff"/><path d="M1 1l5 4 5-4" fill="none" stroke="#fff"/></svg></span><span style="padding-top:5px">hello@veltrix820.io</span></div>
    <div class="contact-row"><span class="ci"><svg width="11" height="14" viewBox="0 0 10 13"><path d="M5 12S1 7 1 4.5a4 4 0 018 0C9 7 5 12 5 12z" fill="none" stroke="#fff" stroke-width="1.4"/></svg></span><span style="padding-top:4px">14 Harbor Lane,<br>Eastfield</span></div>
    <div class="contact-row"><span class="ci"><svg width="14" height="14" viewBox="0 0 24 24"><path d="M6.6 10.8a15 15 0 006.6 6.6l2.2-2.2a1 1 0 011-.25 11.4 11.4 0 003.6.6 1 1 0 011 1V20a1 1 0 01-1 1A17 17 0 013 4a1 1 0 011-1h3.5a1 1 0 011 1c0 1.25.2 2.45.6 3.6a1 1 0 01-.25 1z" fill="#fff"/></svg></span><span style="padding-top:5px">555 0147 2290</span></div>
  </div>
  <div class="f-col" style="left:826px"><h4>Contact Form</h4>
    <div class="field">Name</div>
    <div class="field">Email Address</div>
    <span class="btn" style="position:relative;width:92px;height:38px;font-size:14px;background:var(--navy);color:var(--white)">Submit</span>
  </div>
  <div class="rule"></div>
  <p class="copy">Copyrights @ 2023 Veltrix820. All Rights Reserved.</p>
</footer>

</body>
</html>
```